当募集をご覧頂き誠にありがとうございます。 新商品(BBQグリル)のサムネイル画像を制作して頂ける方を募集します。 <お仕事の詳細> 添付素材のいずれかを用いてサムネイル画像を製作してください。商用利用可能なその他素材を足して頂いても結構です。 画像は一部をズームして切り取ったり、明るさ等を調整頂いたりしてOKです。 本商品の参考サイト http://qelmorstock.com/tk-rz4 http://qelmorstock.com/tkvid <希望イメージ> 文字の視認性、インパクトを重視します。 メインターゲットは40代男性となります。 <コピー> メインコピーとして下記5つの内、一つのみを選択してください ・手軽に本格、叶います BBQグリルの革命児 ・思わず2度見!ファブリックBBQグリル ・お手軽BBQをスタイリッシュに ・ファブリックBBQグリルでスタイリッシュに始めよう! ・サプライズBBQの主役!ファブリックグリル ・常識を覆すファブリックBBQグリル <納品形式> PNGファイルと編集可能なファイル サイズ: 横1600 ×縦900 ピクセル、横1200 × 縦800 ピクセル(2種類) ※横1600×縦900 ピクセルサイズでご提案頂き、採用後に追加で横1200×縦800 ピクセルを製作頂きます。 採用者には必要に応じて高画質画像をお渡しします。 <禁止事項> ・著作権は当方に譲渡されますので、流用・転載・売却は禁止とさせて頂きます。 ・当方が提供する、いかなる情報を許可なく漏洩しないこと。 なお、応募は早期に締め切る可能性があります。 以上、ご応募、お待ちしております。 |
どの案も素敵でしたが、こちらのご提案が一番イメージに近かったため採用させて頂きました。
皆様ご提案ありがとうございます。素敵な案ばかりでした。また機会がございましたらよろしくお願い致します。

```html
<!DOCTYPE html>
<html lang="ja">
<head>
<meta charset="utf-8">
<title>ファブリックBBQグリル サムネイル</title>
<link rel="stylesheet" href="https://fonts.googleapis.com/css2?family=Dela+Gothic+One&family=M+PLUS+1p:wght@800;900&display=swap">
<style>
  :root{
    --red:#e3221c;
    --ink:#0d0d0d;
    --white:#ffffff;
    --sky-top:#b9cfe6;
    --sky-low:#dfe6ea;
    --grass:#6f9a3e;
    --grass-dark:#4b6f28;
    --panel:#0a0a0a;
  }
  *{margin:0;padding:0;box-sizing:border-box}
  html,body{width:1200px;height:674px;overflow:hidden;background:var(--white)}
  .thumb{position:relative;width:1200px;height:674px;overflow:hidden;
    font-family:"M PLUS 1p",sans-serif}
  .park-photo{position:absolute;inset:0;
    background:linear-gradient(180deg,var(--sky-top) 0%,var(--sky-low) 38%,#9fb38a 50%,var(--grass) 62%,var(--grass-dark) 100%)}
  .walker-photo{position:absolute;left:460px;top:80px;width:300px;height:594px;
    background:radial-gradient(ellipse at 50% 50%,rgba(40,50,80,.55) 0%,rgba(40,50,80,.25) 40%,rgba(0,0,0,0) 70%)}
  .grill-photo{position:absolute;left:0;top:360px;width:560px;height:314px;
    background:radial-gradient(ellipse at 55% 40%,#c9b79e 0%,#5a4a3e 35%,#2a2522 65%,#151210 100%);
    border-top-right-radius:40px}
  .dark-panel{position:absolute;inset:0}
  .headline{position:absolute;left:14px;top:70px;transform:rotate(-8deg);transform-origin:left top;
    font-family:"Dela Gothic One",sans-serif;line-height:1;color:var(--white);font-weight:400;
    -webkit-text-stroke:8px var(--ink);paint-order:stroke fill;letter-spacing:-2px}
  .headline .line{display:block;white-space:nowrap}
  .line-lead{font-size:78px}
  .line-lead .accent{font-size:92px}
  .line-main{font-size:124px;margin-top:6px}
  .line-product{font-size:116px;margin-top:10px}
  .line-product .big{font-size:140px}
  .accent{color:var(--red)}
  .features{position:absolute;right:26px;top:30px;list-style:none}
  .features li{display:flex;align-items:center;justify-content:flex-end;gap:14px;
    color:var(--white);font-weight:900;font-size:30px;height:64px;letter-spacing:1px}
  .features svg{width:34px;height:34px;flex:none}
  .products-photo{position:absolute;left:790px;top:250px;width:380px;height:350px;
    background:
      radial-gradient(ellipse at 30% 68%,#d8231d 0%,#a3160f 30%,rgba(0,0,0,0) 48%),
      radial-gradient(ellipse at 70% 30%,#3a3a3a 0%,#1d1d1d 35%,rgba(0,0,0,0) 55%)}
  .color-badge{position:absolute;left:820px;top:350px;width:76px;height:76px;border-radius:50%;
    background:var(--white);color:var(--red);text-align:center;font-weight:900;line-height:1}
  .color-badge b{display:block;font-size:34px;margin-top:10px}
  .color-badge span{display:block;font-size:14px;margin-top:2px}
  .brand{position:absolute;right:30px;bottom:40px;display:flex;align-items:center;gap:10px;
    color:var(--white);font-weight:800;font-size:24px;letter-spacing:2px;line-height:1}
  .brand-dot{width:14px;height:14px;border-radius:50%;background:var(--white)}
</style>
</head>
<body>
<div class="thumb">
  <div class="park-photo" role="img" aria-label="晴れた公園の芝生と遊歩道"></div>
  <div class="walker-photo" role="img" aria-label="赤いグリルを肩に掛けて歩く男性の後ろ姿"></div>
  <div class="grill-photo" role="img" aria-label="網の上でベーコン巻きを焼くファブリックBBQグリルのアップ"></div>

  <svg class="dark-panel" width="1200" height="674" viewBox="0 0 1200 674" aria-hidden="true">
    <polygon points="780,0 1200,0 1200,674 900,674" fill="var(--panel)"/>
  </svg>

  <h1 class="headline">
    <span class="line line-lead">思わず<span class="accent">2度見!</span></span>
    <span class="line line-main">ファブリック</span>
    <span class="line line-product"><span class="accent big">BBQ</span>グリル<span class="accent">!!</span></span>
  </h1>

  <ul class="features">
    <li><svg viewBox="0 0 36 36"><rect x="2" y="8" width="26" height="26" fill="var(--white)"/><path d="M8 20l7 7L33 5" fill="none" stroke="var(--red)" stroke-width="5"/></svg>持ち運びラクラク!!</li>
    <li><svg viewBox="0 0 36 36"><rect x="2" y="8" width="26" height="26" fill="var(--white)"/><path d="M8 20l7 7L33 5" fill="none" stroke="var(--red)" stroke-width="5"/></svg>さっと組み立て!!</li>
    <li><svg viewBox="0 0 36 36"><rect x="2" y="8" width="26" height="26" fill="var(--white)"/><path d="M8 20l7 7L33 5" fill="none" stroke="var(--red)" stroke-width="5"/></svg>手軽にBBQ!!</li>
  </ul>

  <div class="products-photo" role="img" aria-label="赤と黒のファブリックBBQグリル製品写真"></div>
  <div class="color-badge"><b>2</b><span>COLOR</span></div>

  <div class="brand"><span class="brand-dot"></span>FLAMTO GRILLS</div>
</div>
</body>
</html>
```